looking for sleek business card to standout from the crowd!

We are a young biotechnology company looking to help you personalize your health through understanding your genetic make up. We need you help in making a clean but sleek business card design using our new logo. The goal? Any time we give our cards out, people say "nice card!" The feel we are going for is "modern-techy". We don't want to come across as an old, giant pharma company, but not trying to be a hipster either.

Target Market(s)

healthcare and biotechnology industry.

Industry/Entity Type

Biotechnology

Contact Information for Business Card

Info to include on the card will be NAME, TITLE, EMAIL, PHONE. The companies website (www.corvalinbio.com) should also be on the card some where. Would like the logo, when printed, to be raised.

Requirements
Must have
• The logo we have attached in the color it is in. Fonts for text should lean toward more professional/tech.
Nice to have
• Prefer white/light color background
Should not have
• cartoons, landscape backgrounds images.

```html
<!DOCTYPE html>
<html lang="en">
<head>
<meta charset="utf-8">
<title>Corvalin Business Card</title>
<link href="https://fonts.googleapis.com/css2?family=Lato:wght@400;700&display=swap" rel="stylesheet">
<style>
  :root {
    --page-bg: #e9e6e1;
    --card-bg: #f6f5f2;
    --card-edge: #d4d2cd;
    --name-blue: #2a62a6;
    --icon-blue: #1d4f7c;
    --text-dark: #2e2f33;
    --text-muted: #3b3c40;
  }
  html, body {
    margin: 0;
    width: 1200px;
    height: 970px;
    overflow: hidden;
    background: var(--page-bg);
    font-family: "Lato", sans-serif;
  }
  .card {
    position: absolute;
    left: 360px;
    top: 55px;
    width: 480px;
    height: 860px;
    background: var(--card-bg);
    border: 1px solid var(--card-edge);
    box-sizing: border-box;
    overflow: hidden;
  }
  .brand {
    position: absolute;
    left: 57px;
    top: 150px;
    margin: 0;
    font-weight: 700;
    font-size: 48px;
    letter-spacing: 2px;
    color: var(--text-dark);
    line-height: 1;
  }
  .name-tab {
    position: absolute;
    left: 0;
    top: 490px;
    width: 9px;
    height: 66px;
    background: var(--name-blue);
    border-radius: 0 5px 5px 0;
  }
  .person {
    position: absolute;
    left: 51px;
    top: 494px;
  }
  .person-name {
    margin: 0;
    font-weight: 700;
    font-size: 25px;
    color: var(--name-blue);
    letter-spacing: 0.3px;
  }
  .person-title {
    margin: 8px 0 0;
    font-size: 21px;
    color: var(--text-muted);
  }
  .contacts {
    position: absolute;
    left: 53px;
    top: 610px;
    margin: 0;
    padding: 0;
    list-style: none;
  }
  .contacts li {
    display: flex;
    align-items: center;
    height: 41px;
    font-size: 22px;
    color: var(--text-dark);
  }
  .contacts svg {
    width: 22px;
    height: 22px;
    margin-right: 13px;
    fill: var(--icon-blue);
  }
</style>
</head>
<body>
  <div class="card">
    <p class="brand">CORVALIN</p>

    <div class="name-tab"></div>
    <div class="person">
      <p class="person-name">MARLOW TENNANT</p>
      <p class="person-title">Owner</p>
    </div>

    <ul class="contacts">
      <li>
        <svg viewBox="0 0 24 24"><path d="M6.6 10.8c1.4 2.8 3.8 5.1 6.6 6.6l2.2-2.2c.3-.3.7-.4 1-.2 1.1.4 2.3.6 3.6.6.6 0 1 .4 1 1V20c0 .6-.4 1-1 1C10.6 21 3 13.4 3 4c0-.6.4-1 1-1h3.5c.6 0 1 .4 1 1 0 1.3.2 2.5.6 3.6.1.3 0 .7-.2 1z"/></svg>
        123-345-456
      </li>
      <li>
        <svg viewBox="0 0 24 24"><rect x="6" y="2" width="12" height="20" rx="2"/><rect x="8" y="4.5" width="8" height="12" fill="#f6f5f2"/></svg>
        111-222-333
      </li>
      <li>
        <svg viewBox="0 0 24 24"><path d="M3 5h18v14H3z"/><path d="M3 5l9 7 9-7" fill="none" stroke="#f6f5f2" stroke-width="1.8"/></svg>
        yourname@email.com
      </li>
      <li>
        <svg viewBox="0 0 24 24"><circle cx="12" cy="12" r="10"/><path d="M2 12h20M12 2c3 3 3 17 0 20M12 2c-3 3-3 17 0 20" fill="none" stroke="#f6f5f2" stroke-width="1.5"/></svg>
        www.corvalinbio.com
      </li>
    </ul>
  </div>
</body>
</html>
```